Truck wrap - design for fleet

Take our current logo and design a wrap for our fleet of trucks.
Use our website as a guide: brightlane.ca. Trucks are white but can be wrapped fully orange.

Company colors are orange and black

Target Market(s)

Retail

Industry/Entity Type

Paving - driveways etc

Font styles to use
Sans Serif

Colors
F0912C
F2A743
F7CA91
FBE8D2
FDF5EE
EE7325
F08F49
F5BC92
FAE3D3
FDF4ED

Requirements
Must have
• Look awesome

```html
<!DOCTYPE html>
<html lang="en">
<head>
<meta charset="utf-8">
<title>Brightlane Paving – Fleet Wrap</title>
<link rel="stylesheet" href="https://fonts.googleapis.com/css2?family=Montserrat:wght@400;500;600;800&display=swap">
<style>
  :root {
    --ink: #000000;
    --charcoal: #1c1c1c;
    --smoke: #555555;
    --orange-bright: #ff8a00;
    --orange-deep: #d03400;
    --orange-type: #ff5a24;
    --red: #ff0000;
    --red-shade: #b00a0a;
    --white: #ffffff;
  }
  html, body {
    margin: 0;
    padding: 0;
    width: 1200px;
    height: 630px;
    overflow: hidden;
    background: var(--ink);
  }
  .wrap-panel {
    display: block;
    width: 1200px;
    height: 630px;
  }
  .brand-name {
    font-family: "Montserrat", sans-serif;
    font-weight: 800;
    fill: var(--white);
  }
  .brand-trade {
    font-family: "Montserrat", sans-serif;
    font-weight: 400;
    fill: var(--orange-type);
  }
  .services {
    font-family: "Montserrat", sans-serif;
    font-weight: 500;
    fill: var(--white);
  }
  .web-address {
    font-family: "Montserrat", sans-serif;
    font-weight: 600;
    fill: var(--white);
  }
  .badge-name {
    font-family: "Montserrat", sans-serif;
    font-weight: 800;
    fill: var(--white);
  }
</style>
</head>
<body>
<svg class="wrap-panel" viewBox="0 0 1200 630" xmlns="http://www.w3.org/2000/svg" aria-label="Brightlane Paving fleet wrap">
  <defs>
    <linearGradient id="bg-fade" x1="0" y1="0" x2="0" y2="1">
      <stop offset="0" stop-color="var(--charcoal)"/>
      <stop offset="1" stop-color="var(--ink)"/>
    </linearGradient>
    <radialGradient id="bg-glow" cx="400" cy="0" r="520" gradientUnits="userSpaceOnUse">
      <stop offset="0" stop-color="var(--smoke)"/>
      <stop offset="1" stop-color="var(--smoke)" stop-opacity="0"/>
    </radialGradient>
    <radialGradient id="bg-glow-right" cx="960" cy="100" r="380" gradientUnits="userSpaceOnUse">
      <stop offset="0" stop-color="#3a3a3a"/>
      <stop offset="1" stop-color="#3a3a3a" stop-opacity="0"/>
    </radialGradient>
    <linearGradient id="chevron-fill" x1="0" y1="0" x2="0" y2="1">
      <stop offset="0.4" stop-color="var(--orange-bright)"/>
      <stop offset="1" stop-color="var(--orange-deep)"/>
    </linearGradient>
    <linearGradient id="band-left-fill" x1="0" y1="0" x2="1" y2="0">
      <stop offset="0" stop-color="var(--orange-deep)"/>
      <stop offset="1" stop-color="var(--orange-bright)"/>
    </linearGradient>
    <linearGradient id="band-right-fill" x1="554" y1="0" x2="1200" y2="0" gradientUnits="userSpaceOnUse">
      <stop offset="0" stop-color="#3a1200"/>
      <stop offset="0.2" stop-color="var(--orange-deep)"/>
      <stop offset="1" stop-color="var(--orange-bright)"/>
    </linearGradient>
  </defs>

  <!-- background -->
  <rect class="backdrop" width="1200" height="630" fill="url(#bg-fade)"/>
  <rect class="backdrop-glow" width="1200" height="630" fill="url(#bg-glow)"/>
  <rect class="backdrop-glow" width="1200" height="630" fill="url(#bg-glow-right)"/>

  <!-- bands -->
  <polygon class="band-bottom-left" points="0,504 521,504 396,630 0,630" fill="url(#band-left-fill)"/>
  <polygon class="band-bottom-right" points="603,581 1200,581 1200,630 554,630" fill="url(#band-right-fill)"/>
  <polygon class="chevron" points="419,0 531,0 846,315 531,630 419,630 734,315" fill="url(#chevron-fill)"/>

  <!-- web address tab -->
  <polygon class="web-tab-shade" points="859,75 1200,75 1200,103 887,103" fill="var(--red-shade)"/>
  <polygon class="web-tab" points="640,0 1200,0 1200,75 714,75" fill="var(--red)"/>
  <text class="web-address" x="948" y="50" font-size="52" text-anchor="middle">brightlane.ca</text>

  <!-- wordmark -->
  <text class="brand-name" x="316" y="252" font-size="80" text-anchor="middle" textLength="430" lengthAdjust="spacingAndGlyphs">BRIGHTLANE</text>
  <text class="brand-trade" x="315" y="347" font-size="96" text-anchor="middle" textLength="364" lengthAdjust="spacing">PAVING</text>
  <text class="services" x="315" y="405" font-size="34" text-anchor="middle" textLength="586" lengthAdjust="spacing">Driveways • Paving • Asphalt Repair</text>

  <!-- name badge -->
  <text class="badge-name" x="1011" y="336" font-size="54" text-anchor="middle" textLength="290" lengthAdjust="spacingAndGlyphs">brightlane</text>
</svg>
</body>
</html>
```